business card design for luxurious real estate brand

using the attached logo, i am looking for a 2-sided business card design. the back should be the gold logo on black background. the front needs to include: gold logo, name, phone, email, and website

Industry/Entity Type

real estate

Contact Information for Business Card

logo, name, email, phone, website

Font styles to use
Sans Serif

```html
<!DOCTYPE html>
<html lang="en">
<head>
<meta charset="utf-8">
<title>Maison Corvell – Business Card</title>
<link rel="stylesheet" href="https://fonts.googleapis.com/css2?family=Open+Sans:wght@400;600;700&display=swap">
<style>
  :root {
    --stage: #d9d4cc;
    --card-black: #070707;
    --pattern-dark: #1d1d1d;
    --gold: #f0c20c;
    --gold-line: #8a700c;
    --text-light: #e9e9e9;
  }
  * { box-sizing: border-box; margin: 0; padding: 0; }
  html, body {
    width: 1200px; height: 900px; overflow: hidden;
    background: var(--stage);
    font-family: "Open Sans", Arial, sans-serif;
  }
  .stage {
    width: 1200px; height: 900px;
    display: flex; flex-direction: column; align-items: center; justify-content: center;
    gap: 36px;
  }
  .card {
    width: 700px; height: 400px;
    background: var(--card-black);
    position: relative;
    overflow: hidden;
    box-shadow: 0 10px 28px rgba(0,0,0,0.35);
  }

  /* Back side */
  .card-back__pattern {
    position: absolute; inset: 0;
    background: linear-gradient(135deg, var(--card-black) 0%, var(--pattern-dark) 50%, var(--card-black) 100%);
  }
  .card-back__wordmark {
    position: absolute; left: 430px; top: 150px;
    color: var(--gold);
    font-weight: 600;
    font-size: 22px;
    letter-spacing: 4px;
    text-transform: uppercase;
  }

  /* Front side */
  .brand {
    position: absolute; left: 380px; top: 92px;
    display: flex; align-items: center; gap: 14px;
  }
  .brand__square {
    width: 22px; height: 22px; background: var(--gold);
  }
  .brand__name {
    color: var(--gold);
    font-weight: 600;
    font-size: 26px;
    letter-spacing: 6px;
    text-transform: uppercase;
  }
  .holder {
    position: absolute; left: 40px; top: 290px;
    display: flex; align-items: baseline; gap: 8px;
  }
  .holder__name {
    color: var(--gold); font-weight: 700; font-size: 19px; text-transform: uppercase;
  }
  .holder__divider { color: var(--gold); font-weight: 700; font-size: 20px; }
  .holder__title { color: var(--text-light); font-size: 16px; }
  .rule {
    position: absolute; left: 40px; right: 40px; top: 326px;
    height: 1px; background: var(--gold-line);
  }
  .contacts {
    position: absolute; left: 40px; top: 340px;
    display: flex; align-items: center; gap: 10px;
    color: var(--text-light); font-size: 15px;
  }
  .contact { display: flex; align-items: center; gap: 7px; }
  .contact__icon { width: 16px; height: 16px; fill: var(--gold); }
  .contacts__sep { color: var(--text-light); }
</style>
</head>
<body>
<main class="stage">

  <section class="card card-back" aria-label="Card back">
    <div class="card-back__pattern" role="img" aria-label="Dark tonal repeating monogram pattern"></div>
    <span class="card-back__wordmark">Maison Corvell</span>
  </section>

  <section class="card card-front" aria-label="Card front">
    <div class="brand">
      <span class="brand__square"></span>
      <span class="brand__name">Maison Corvell</span>
    </div>

    <div class="holder">
      <span class="holder__name">Elena Marsh</span>
      <span class="holder__divider">|</span>
      <span class="holder__title">Director</span>
    </div>
    <div class="rule"></div>

    <div class="contacts">
      <span class="contact">
        <svg class="contact__icon" viewBox="0 0 16 16" aria-hidden="true">
          <path d="M1 5c0-2 3-3 7-3s7 1 7 3v1.5h-3.5V5h-7v1.5H1z"/>
          <path d="M3 8h10l1 6H2z"/>
        </svg>
        555-014-2278
      </span>
      <span class="contacts__sep">|</span>
      <span class="contact">
        <svg class="contact__icon" viewBox="0 0 16 16" aria-hidden="true">
          <path d="M1 6l7-4 7 4v8H1z"/>
          <path d="M2 6.5l6 4 6-4" fill="none" stroke="#070707" stroke-width="1.2"/>
        </svg>
        info@maisoncorvell.com
      </span>
      <span class="contacts__sep">|</span>
      <span class="contact">
        <svg class="contact__icon" viewBox="0 0 16 16" aria-hidden="true">
          <circle cx="8" cy="8" r="7"/>
          <path d="M1 8h14M8 1c-3 3.5-3 10.5 0 14M8 1c3 3.5 3 10.5 0 14" fill="none" stroke="#070707" stroke-width="1"/>
        </svg>
        www.maisoncorvell.com
      </span>
    </div>
  </section>

</main>
</body>
</html>
```